Updated Business Cards

We need to update our business cards to reflect new services and employees. We are a luxury vacation rental company in Sandpoint, Idaho. Would also like to make the front facing font easier to read (larger fonts) I love the original logo created for our company and want to use this for the back of the business card created like before - with the dark blue color. See previous files.

Front of the card needs to include:
Employee Name
Title
Phone: 555-555-0147 (ext X)
Address: 418 W. Larkmoor St, Ste 5
Brightwater, ST 00000
Book Direct: www.RestWillowbay.example

```html
<!DOCTYPE html>
<html lang="en">
<head>
<meta charset="utf-8">
<title>Carrow Management – Business Cards</title>
<link href="https://fonts.googleapis.com/css2?family=Montserrat:wght@400;500;600;700&display=swap" rel="stylesheet">
<style>
  :root {
    --page-bg: #2b2b2e;
    --card-dark: #0e0e16;
    --card-white: #ffffff;
    --navy: #26306e;
    --navy-light: #3b4aa0;
    --ink: #1c1c22;
  }
  * { box-sizing: border-box; margin: 0; padding: 0; }
  html, body { width: 1200px; height: 900px; overflow: hidden; }
  body {
    background: var(--page-bg);
    font-family: "Montserrat", sans-serif;
    display: flex;
    flex-direction: column;
    align-items: center;
    justify-content: center;
    gap: 40px;
  }
  .card {
    position: relative;
    width: 640px;
    height: 366px;
    border-radius: 22px;
    overflow: hidden;
    box-shadow: 0 10px 30px rgba(0,0,0,.45);
  }
  .card-back {
    background: var(--card-dark);
    display: flex;
    align-items: center;
    justify-content: center;
  }
  .wordmark {
    display: flex;
    align-items: center;
    gap: 14px;
    color: var(--navy);
    font-weight: 600;
    letter-spacing: .08em;
    text-transform: uppercase;
  }
  .wordmark-square { width: 22px; height: 22px; background: var(--navy); }
  .card-back .wordmark { font-size: 30px; color: var(--navy-light); }
  .card-back .wordmark-square { background: var(--navy-light); width: 26px; height: 26px; }
  .card-front { background: var(--card-white); }
  .front-wave {
    position: absolute;
    left: 0; bottom: 0;
    width: 640px; height: 130px;
  }
  .front-logo {
    position: absolute;
    top: 54px; left: 0; right: 0;
    display: flex;
    justify-content: center;
  }
  .front-logo .wordmark { font-size: 26px; }
  .front-details {
    position: absolute;
    top: 128px; left: 0; right: 0;
    display: flex;
    justify-content: center;
    align-items: center;
    gap: 18px;
  }
  .person { text-align: right; }
  .person-name { color: var(--navy); font-weight: 700; font-size: 24px; line-height: 1.1; }
  .person-title { color: var(--ink); font-size: 15px; margin-top: 4px; }
  .divider { width: 2px; height: 78px; background: var(--navy); }
  .contact-list { list-style: none; display: flex; flex-direction: column; gap: 7px; }
  .contact-item {
    display: flex; align-items: center; gap: 9px;
    font-size: 14px; color: var(--ink);
  }
  .contact-icon { width: 14px; height: 14px; fill: var(--navy); flex: none; }
  .address {
    position: absolute;
    top: 232px; left: 0; right: 0;
    text-align: center;
    font-size: 15px;
    color: var(--ink);
  }
</style>
</head>
<body>

  <section class="card card-back" aria-label="Card back">
    <div class="wordmark"><span class="wordmark-square"></span>Carrow Management</div>
  </section>

  <section class="card card-front" aria-label="Card front">
    <svg class="front-wave" viewBox="0 0 640 130" preserveAspectRatio="none" aria-hidden="true">
      <path d="M0 118 C 220 110 450 80 640 10 L640 130 L0 130 Z" fill="#0b0b10"/>
      <path d="M0 110 C 220 102 450 72 640 2" fill="none" stroke="#26306e" stroke-width="3"/>
    </svg>

    <div class="front-logo">
      <div class="wordmark"><span class="wordmark-square"></span>Carrow Management</div>
    </div>

    <div class="front-details">
      <div class="person">
        <p class="person-name">Dana Whitfield</p>
        <p class="person-title">Managing Director</p>
      </div>
      <div class="divider"></div>
      <ul class="contact-list">
        <li class="contact-item">
          <svg class="contact-icon" viewBox="0 0 24 24"><path d="M6.6 10.8a15.1 15.1 0 0 0 6.6 6.6l2.2-2.2c.3-.3.7-.4 1-.2 1.1.4 2.3.6 3.6.6.6 0 1 .4 1 1V20c0 .6-.4 1-1 1A17 17 0 0 1 3 4c0-.6.4-1 1-1h3.5c.6 0 1 .4 1 1 0 1.3.2 2.5.6 3.6.1.3 0 .7-.2 1z"/></svg>
          555-555-0147 (ext X)
        </li>
        <li class="contact-item">
          <svg class="contact-icon" viewBox="0 0 24 24"><path d="M2 5h20v14H2z"/><path d="M3 6l9 7 9-7" fill="none" stroke="#fff" stroke-width="1.6"/></svg>
          info@RestWillowbay.example
        </li>
        <li class="contact-item">
          <svg class="contact-icon" viewBox="0 0 24 24"><circle cx="12" cy="12" r="10"/><path d="M2 12h20M12 2c3 3 3 17 0 20M12 2c-3 3-3 17 0 20" fill="none" stroke="#fff" stroke-width="1.4"/></svg>
          www.RestWillowbay.example
        </li>
      </ul>
    </div>

    <p class="address">418 W. Larkmoor St, Ste 5 Brightwater, ST 00000</p>
  </section>

</body>
</html>
```